LOGO and WEBSITE Design for Velmora-Kast

We need a LOGO and WEBSITE design (Wordpress) with online store for a genetic testing company for athletes. The colors should be more masculine though appeal to both men and women.
Updates

Name of company updated (to Velmora-Kast) for the LOGO and WEBSITE design.

Target Market(s)

Performance and endurance Athletes. College and pro athletes. Male and Female.

Industry/Entity Type

Fitness. Wellness. Sports.

Coding

Coded - Design and coding required

Number of Pages Required

5+ page

Requirements
Must have
• Call to action(s) to order the genetic tests. A space on the Home page that shows an example of a customized genetic report.
Should not have
• Bright colors. Template looking. All black website. Clip art logos.

```html
<!DOCTYPE html>
<html lang="en">
<head>
<meta charset="utf-8">
<title>Velmora-Kast — Genetic Testing for Athletes</title>
<link href="https://fonts.googleapis.com/css2?family=Montserrat:wght@400;500;600;700&display=swap" rel="stylesheet">
<style>
:root{
  --navy:#1c1b45;
  --purple:#3a1f5e;
  --lavender:#ebecf9;
  --lavender-bar:#c9cbea;
  --ice:#eef1fc;
  --ink:#222233;
  --muted:#555566;
  --grey-btn:#d9dbe3;
  --accent-green:#b9c96f;
  --icon-blue:#2e3b8f;
  --widget-blue:#e2ebfb;
  --cyan:#19a6d6;
  --blue:#1f7fe0;
  --ok:#2b8a57;
  --warn:#c98a1a;
  --white:#ffffff;
}
*{box-sizing:border-box;margin:0;padding:0}
html,body{width:1200px;height:3592px;overflow:hidden}
body{position:relative;background:var(--white);font-family:"Montserrat",Arial,sans-serif;color:var(--ink)}
a{text-decoration:none}
.abs{position:absolute}

/* header + hero */
.hero{left:0;top:0;width:1200px;height:620px;clip-path:polygon(0 0,100% 0,100% 96%,0 88%);
  background:linear-gradient(115deg,#4a2a6e 0%,#2a1f55 40%,#1c1b45 70%,#232a5c 100%)}
.hero-art{left:0;top:120px;width:700px;height:420px;background:radial-gradient(ellipse at 40% 45%,rgba(140,110,200,.45),rgba(40,25,80,0) 70%)}
.nav{left:0;top:0;width:1200px;height:120px}
.logo{left:140px;top:32px;color:var(--white);font-weight:700;font-size:34px;letter-spacing:1px}
.nav-link{top:40px;color:var(--white);font-weight:600;font-size:22px}
.cta{left:880px;top:26px;width:184px;height:50px;background:var(--grey-btn);color:var(--navy);font-weight:600;font-size:22px;display:flex;align-items:center;justify-content:center;border-radius:3px}
.hero-title{left:708px;top:196px;color:var(--white);font-weight:700;font-size:42px;line-height:50px}
.hero-text{left:708px;top:310px;width:380px;color:#e7e6f3;font-size:18px;line-height:26px}
.btn-grey{left:708px;top:412px;width:232px;height:60px;background:#c9cad4;color:var(--navy);font-size:18px;font-weight:500;display:flex;align-items:center;justify-content:center;border-radius:3px}

.h2{font-weight:600;font-size:36px;color:var(--ink)}
.body{font-size:18px;line-height:26px;color:var(--muted)}
.btn-dark{height:44px;background:var(--navy);color:var(--white);font-size:16px;font-weight:600;display:flex;align-items:center;justify-content:center;border-radius:3px}

.about-photo{left:580px;top:604px;width:486px;height:416px;background:linear-gradient(135deg,#c9d4dc,#7e96a8 60%,#3b5466)}

/* services */
.services{left:0;top:1120px;width:1200px;height:510px;background:var(--lavender)}
.svc-title{left:0;top:1178px;width:1200px;text-align:center}
.svc-num{font-size:18px;color:#333;width:60px;text-align:center}
.svc-name{font-size:20px;font-weight:500;text-align:center;width:240px}
.svc-text{font-size:16px;line-height:22px;color:var(--muted);text-align:center;width:240px}

.flex-art{left:140px;top:1738px;width:334px;height:404px;background:var(--ice)}

/* sample report */
.plan{left:0;top:2255px;width:1200px;height:620px;clip-path:polygon(0 0,100% 0,100% 58%,0 72%);
  background:linear-gradient(120deg,#1c2a3a 0%,#213d4a 45%,#1b2a36 100%)}
.plan-title{left:0;top:2318px;width:1200px;text-align:center;color:var(--white);font-weight:600;font-size:34px}
.report{left:255px;top:2370px;width:746px;height:496px;background:var(--white);border:1px solid #c8ccd6;border-radius:4px;box-shadow:0 4px 14px rgba(0,0,0,.25);font-size:15px;color:#222}
.r-head{left:0;top:0;width:744px;height:44px;background:var(--widget-blue);border-bottom:1px solid #c8d3ea;padding:12px 14px;color:#1a4da0}
.r-seg{top:96px;height:36px;display:flex;align-items:center;justify-content:center;color:#fff}
.r-row{left:0;width:744px;height:50px;border-top:1px solid #d6d9e0;padding:16px 14px}
.chev{position:absolute;right:16px;top:18px}
.badge{position:absolute;right:48px;top:14px;font-size:12px;color:#fff;padding:3px 7px;border-radius:3px}

/* order */
.order{left:325px;top:2965px;width:560px;height:218px;background:var(--white);border:1px solid #c9ccd6;border-radius:8px;box-shadow:0 2px 10px rgba(0,0,0,.12)}
.order-title{left:0;top:26px;width:560px;text-align:center;font-size:22px;font-weight:600}
.field{left:50px;width:180px;height:24px;border:1px solid #aaa;border-radius:3px;font-size:11px;color:#777;padding:4px 8px}
.submit{left:230px;top:144px;width:76px;height:30px;background:var(--navy);color:#fff;font-size:12px;display:flex;align-items:center;justify-content:center;border-radius:3px}

/* footer */
.footer{left:0;top:3070px;width:1200px;height:476px;clip-path:polygon(0 14%,100% 0,100% 100%,0 100%);
  background:linear-gradient(100deg,#221f52 0%,#2e2a63 45%,#6c6f85 100%)}
.f-head{top:3282px;color:var(--white);font-weight:600;font-size:22px}
.f-link{color:#e3e3ee;font-size:16px}
.f-logo{left:868px;top:3280px;color:#fff;font-weight:700;font-size:30px}
.f-text{left:752px;top:3334px;width:320px;text-align:center;color:#e3e3ee;font-size:14px;line-height:20px}
.social{top:3418px;width:36px;height:36px;border-radius:50%;background:#4a5bc8}
.bottom-bar{left:0;top:3546px;width:1200px;height:46px;background:var(--lavender-bar);text-align:center;font-size:15px;line-height:46px;color:#333}
</style>
</head>
<body>

<header>
  <div class="abs hero"></div>
  <div class="abs hero-art" role="img" aria-label="Glowing DNA double helix imagery on deep purple"></div>
  <nav class="abs nav">
    <div class="abs logo">LOGO</div>
    <a class="abs nav-link" style="left:460px">Home</a>
    <a class="abs nav-link" style="left:575px">Online Store</a>
    <a class="abs nav-link" style="left:760px">Services</a>
    <a class="abs cta">Call to Action</a>
  </nav>
  <h1 class="abs hero-title">Gentic Testing<br>Company</h1>
  <p class="abs hero-text">DNA-based training insight for college and pro athletes, men and women.</p>
  <a class="abs btn-grey">Get Started</a>
</header>

<section class="about">
  <h2 class="abs h2" style="left:140px;top:676px">About Us</h2>
  <p class="abs body" style="left:140px;top:740px;width:390px">Lorem ipsum dolor sit amet, consectetur adipiscing elit, sed do eiusmod tempor incididunt ut labore et dolore magna aliqua. Quis ipsum suspendisse ultrices gravida. Risus commodo viverra maecenas accumsan lacus vel facilisis.</p>
  <a class="abs btn-dark" style="left:140px;top:940px;width:190px">Learn More</a>
  <div class="abs about-photo" role="img" aria-label="Lab scientist in white coat working with samples"></div>
</section>

<section>
  <div class="abs services"></div>
  <h2 class="abs h2 svc-title">Our Services</h2>
  <svg class="abs" style="left:0;top:1230px" width="1200" height="340" viewBox="0 0 1200 340">
    <path d="M140 140 A160 160 0 0 1 445 100" fill="none" stroke="var(--accent-green)" stroke-width="2"/>
    <path d="M445 200 A165 165 0 0 0 755 200" fill="none" stroke="var(--accent-green)" stroke-width="2"/>
    <path d="M755 100 A160 160 0 0 1 1060 140" fill="none" stroke="var(--accent-green)" stroke-width="2"/>
    <g fill="var(--icon-blue)">
      <circle cx="300" cy="113" r="20" fill="#fff"/>
      <path d="M300 122 l-9-9 a5 5 0 0 1 9-6 a5 5 0 0 1 9 6z"/>
      <circle cx="600" cy="83" r="20" fill="#fff"/>
      <rect x="592" y="74" width="6" height="16"/><rect x="601" y="78" width="6" height="12"/>
      <circle cx="910" cy="113" r="20" fill="#fff"/>
      <circle cx="910" cy="106" r="5"/><rect x="901" y="113" width="18" height="9" rx="4"/>
    </g>
  </svg>
  <div class="abs svc-num" style="left:270px;top:1282px">01.</div>
  <div class="abs svc-name" style="left:180px;top:1428px">Heart Health</div>
  <p class="abs svc-text" style="left:180px;top:1464px">Lorem ipsum dolor sit amet, consectetur adipiscing elit, sed do eiusmod tempor .</p>
  <div class="abs svc-name" style="left:480px;top:1380px">Universal Testing</div>
  <p class="abs svc-text" style="left:480px;top:1416px">Lorem ipsum dolor sit amet, consectetur adipiscing elit, sed do eiusmod tempor .</p>
  <div class="abs svc-num" style="left:570px;top:1516px">02.</div>
  <div class="abs svc-num" style="left:880px;top:1282px">03.</div>
  <div class="abs svc-name" style="left:790px;top:1428px">Counseling</div>
  <p class="abs svc-text" style="left:790px;top:1464px">Lorem ipsum dolor sit amet, consectetur adipiscing elit, sed do eiusmod tempor .</p>
</section>

<section>
  <div class="abs flex-art" role="img" aria-label="Illustration of a hand holding a gear with a check mark and a coin"></div>
  <h2 class="abs h2" style="left:664px;top:1794px">Flexible Cost</h2>
  <p class="abs body" style="left:664px;top:1858px;width:400px">Lorem ipsum dolor sit amet, consectetur adipiscing elit, sed do eiusmod tempor incididunt ut labore et dolore magna aliqua. Quis ipsum suspendisse ultrices gravida. Risus commodo viverra maecenas accumsan lacus vel facilisis.</p>
  <a class="abs btn-dark" style="left:664px;top:2064px;width:150px">Learn More</a>
</section>

<section>
  <div class="abs plan" role="img" aria-label="Dark teal background with blurred DNA strands"></div>
  <h2 class="abs plan-title">Customized Plan</h2>
  <div class="abs report" aria-label="Example genetic report">
    <div class="abs r-head">Sample Athlete Report
      <svg class="chev" style="top:16px" width="14" height="9" viewBox="0 0 14 9"><path d="M1 8 7 2 13 8" fill="none" stroke="#333" stroke-width="2"/></svg>
    </div>
    <div class="abs" style="left:14px;top:70px">Athlete profile: distance runner, female, 24 — focus area:</div>
    <div class="abs r-seg" style="left:14px;width:88px;background:var(--cyan)">Power</div>
    <div class="abs r-seg" style="left:102px;width:262px;background:var(--blue)">Endurance</div>
    <div class="abs r-seg" style="left:364px;width:140px;color:#222">Recovery</div>
    <div class="abs r-seg" style="left:510px;width:210px;background:#222">Injury Risk</div>
    <div class="abs" style="left:14px;top:152px">Genes analysed for this athlete's training plan:</div>
    <div class="abs" style="left:14px;top:178px;width:706px;height:30px;border:1px solid #bbb;border-radius:3px;display:flex;align-items:center">
      <span style="background:#e9e9ee;height:100%;padding:5px 12px;border-right:1px solid #bbb">Panel A</span><span style="padding-left:10px">ACTN3 · ACE · PPARGC1A · COL5A1</span>
    </div>
    <div class="abs r-row" style="top:240px">Muscle fibre type<span class="badge" style="background:var(--cyan)">Mixed</span><svg class="chev" width="14" height="9" viewBox="0 0 14 9"><path d="M1 1 7 7 13 1" fill="none" stroke="#333" stroke-width="2"/></svg></div>
    <div class="abs r-row" style="top:290px">VO2 max training response<span class="badge" style="background:var(--ok)">High</span><svg class="chev" width="14" height="9" viewBox="0 0 14 9"><path d="M1 1 7 7 13 1" fill="none" stroke="#333" stroke-width="2"/></svg></div>
    <div class="abs r-row" style="top:340px">Recovery speed<span class="badge" style="background:var(--ok)">Fast</span><svg class="chev" width="14" height="9" viewBox="0 0 14 9"><path d="M1 1 7 7 13 1" fill="none" stroke="#333" stroke-width="2"/></svg></div>
    <div class="abs r-row" style="top:390px">Tendon injury risk<span class="badge" style="background:var(--warn)">Moderate</span><svg class="chev" width="14" height="9" viewBox="0 0 14 9"><path d="M1 1 7 7 13 1" fill="none" stroke="#333" stroke-width="2"/></svg></div>
  </div>
</section>

<footer>
  <div class="abs footer"></div>
  <section class="abs order">
    <h2 class="abs order-title">Make an Order</h2>
    <div class="abs field" style="top:74px">Full Name</div>
    <div class="abs field" style="top:106px">Email</div>
    <a class="abs submit">Submit</a>
  </section>

  <div class="abs f-head" style="left:135px">Pages</div>
  <a class="abs f-link" style="left:135px;top:3338px">Home</a>
  <a class="abs f-link" style="left:135px;top:3378px">Online Store</a>
  <a class="abs f-link" style="left:135px;top:3418px">Services</a>

  <div class="abs f-head" style="left:270px">Comunity</div>
  <a class="abs f-link" style="left:270px;top:3338px">Friendline</a>
  <a class="abs f-link" style="left:270px;top:3378px">Chirper</a>
  <a class="abs f-link" style="left:270px;top:3418px">Snapgrid</a>
  <a class="abs f-link" style="left:270px;top:3458px">Workweb</a>

  <div class="abs f-head" style="left:446px">LEGAL</div>
  <a class="abs f-link" style="left:446px;top:3338px">Privacy Policy</a>
  <a class="abs f-link" style="left:446px;top:3378px">Terms of Service</a>
  <a class="abs f-link" style="left:446px;top:3418px">Cookies</a>

  <div class="abs f-logo">LOGO</div>
  <p class="abs f-text">Lorem ipsum dolor sit amet, consectetur adipiscing elit, sed do eiusmod tempor incididunt ut la</p>
  <span class="abs social" style="left:810px"></span>
  <span class="abs social" style="left:868px"></span>
  <span class="abs social" style="left:926px"></span>
  <span class="abs social" style="left:984px"></span>

  <div class="abs bottom-bar">Velmora-Kast © 2024</div>
</footer>

</body>
</html>
```